Business Card Design

Locksmith, Safes, Security Systems, Camera Systems, Home Theater, Chip Keys & Remotes

Industry/Entity Type

Business

Contact Information for Business Card

Dorian Pelley Owner
2870 Fenwick Hollow Loop
Dothan, AL 36301
P 334-555-0148
F 334-555-0193
dpelley@tamblynkeys.com
www.tamblynkeys.com
AL Lic #5827
*Maybe follow us on Linkfeed or Linkfeed symbol

```html
<!DOCTYPE html>
<html lang="en">
<head>
<meta charset="utf-8">
<title>Tamblyn's Lock &amp; Security – Business Card</title>
<link rel="stylesheet" href="https://fonts.googleapis.com/css2?family=Lato:wght@400;700&display=swap">
<style>
  :root {
    --card-bg: #ecebe6;
    --brand-blue: #2b3a91;
    --ink-light: #ffffff;
    --hole-fill: #ffffff;
  }
  html, body {
    margin: 0;
    padding: 0;
    width: 1200px;
    height: 702px;
    overflow: hidden;
    background: var(--card-bg);
  }
  .card {
    position: relative;
    width: 1200px;
    height: 702px;
    background: var(--card-bg);
    font-family: "Lato", sans-serif;
    overflow: hidden;
  }
  .tag-shape {
    position: absolute;
    inset: 0;
  }
  .brand {
    position: absolute;
    left: 36px;
    top: 300px;
    display: flex;
    align-items: center;
    gap: 40px;
    color: var(--brand-blue);
    font-weight: 700;
  }
  .brand-square {
    width: 134px;
    height: 134px;
    background: var(--brand-blue);
    border-radius: 4px;
  }
  .brand-name {
    display: flex;
    flex-direction: column;
    align-items: center;
    line-height: 1;
  }
  .brand-title {
    font-size: 56px;
    letter-spacing: 1px;
    text-transform: uppercase;
  }
  .brand-sub {
    margin-top: 12px;
    font-size: 22px;
    letter-spacing: 1px;
    text-transform: uppercase;
  }
  .contact {
    position: absolute;
    right: 64px;
    color: var(--ink-light);
    text-align: right;
    line-height: 1;
  }
  .person-name {
    top: 82px;
    font-size: 46px;
    letter-spacing: 0.5px;
  }
  .person-role {
    top: 134px;
    right: 68px;
    font-size: 30px;
  }
  .divider {
    position: absolute;
    left: 583px;
    right: 64px;
    top: 194px;
    height: 1px;
    background: var(--ink-light);
  }
  .licence {
    top: 211px;
    right: 69px;
    font-size: 18px;
  }
  .contact-row {
    position: absolute;
    right: 64px;
    display: flex;
    align-items: center;
    gap: 22px;
    color: var(--ink-light);
    text-align: right;
  }
  .contact-text {
    font-size: 25px;
    line-height: 36px;
  }
  .icon {
    width: 38px;
    display: flex;
    justify-content: center;
  }
  .row-address { top: 296px; }
  .row-phone { top: 366px; }
  .row-web { top: 462px; }
  .follow {
    position: absolute;
    right: 64px;
    top: 612px;
    display: flex;
    align-items: baseline;
    gap: 18px;
    color: var(--ink-light);
    font-size: 27px;
  }
  .social-name {
    font-size: 20px;
  }
</style>
</head>
<body>
<div class="card">
  <svg class="tag-shape" width="1200" height="702" viewBox="0 0 1200 702" aria-hidden="true">
    <defs>
      <radialGradient id="hole-shade" cx="50%" cy="65%" r="60%">
        <stop offset="0%" stop-color="#ffffff"/>
        <stop offset="70%" stop-color="#f2f2f0"/>
        <stop offset="100%" stop-color="#1a1a1a"/>
      </radialGradient>
    </defs>
    <path d="M581,0 H1200 V702 H597 L536,641 V254 C484,236 456,180 461,124 C467,58 518,6 581,0 Z" fill="var(--brand-blue)"/>
    <circle cx="555" cy="135" r="19" fill="url(#hole-shade)"/>
  </svg>

  <div class="brand">
    <div class="brand-square"></div>
    <div class="brand-name">
      <span class="brand-title">Tamblyn's</span>
      <span class="brand-sub">Lock &amp; Security</span>
    </div>
  </div>

  <div class="contact person-name">DORIAN PELLEY</div>
  <div class="contact person-role">Owner</div>
  <div class="divider"></div>
  <div class="contact licence">AL Lic #5827</div>

  <div class="contact-row row-address">
    <div class="contact-text">2870 Fenwick Hollow Loop Dothan, AL 36301</div>
    <div class="icon">
      <svg width="30" height="44" viewBox="0 0 30 44" aria-hidden="true">
        <path d="M15,0 C6.7,0 0,6.7 0,15 C0,26 15,44 15,44 C15,44 30,26 30,15 C30,6.7 23.3,0 15,0 Z M15,21 A6,6 0 1,1 15,9 A6,6 0 1,1 15,21 Z" fill="var(--ink-light)"/>
      </svg>
    </div>
  </div>

  <div class="contact-row row-phone">
    <div class="contact-text">P 334-555-0148<br>F 334-555-0193</div>
    <div class="icon">
      <svg width="26" height="42" viewBox="0 0 26 42" aria-hidden="true">
        <rect x="0" y="0" width="26" height="42" rx="5" fill="var(--ink-light)"/>
        <rect x="4" y="6" width="18" height="26" fill="var(--brand-blue)"/>
        <circle cx="13" cy="37" r="2.3" fill="var(--brand-blue)"/>
      </svg>
    </div>
  </div>

  <div class="contact-row row-web">
    <div class="contact-text">dpelley@tamblynkeys.com<br>www.tamblynkeys.com</div>
    <div class="icon">
      <svg width="38" height="28" viewBox="0 0 38 28" aria-hidden="true">
        <rect x="0" y="0" width="38" height="28" rx="3" fill="var(--ink-light)"/>
        <path d="M1,3 L19,16 L37,3" fill="none" stroke="var(--brand-blue)" stroke-width="2.5"/>
      </svg>
    </div>
  </div>

  <div class="follow">
    <span>Follow us on</span>
    <span class="social-name">Linkfeed</span>
    <span class="social-name">Chirper</span>
  </div>
</div>
</body>
</html>
```